Advertisement Sign

Hello,
We're in need of a new design for an advertisement sign. Below is our current concept, but we're looking for improvements. Specifically, we'd like to enhance the size of the 'Call for Assistance' text, possibly explore different fonts, and possibly add a background to make the design more engaging and less plain. We need something that sticks out more. Any suggestions are welcome.

Target Market(s)

Construction and Landscape Companies

```html
<!DOCTYPE html>
<html lang="en">
<head>
<meta charset="utf-8">
<title>Tallon Sign</title>
<link href="https://fonts.googleapis.com/css2?family=Unbounded:wght@800;900&display=swap" rel="stylesheet">
<style>
  :root {
    --page: #ffffff;
    --charcoal: #2b2b2b;
    --brand-blue: #2b75bb;
    --white: #ffffff;
  }
  * { margin: 0; padding: 0; box-sizing: border-box; }
  html, body {
    width: 976px;
    height: 1200px;
    overflow: hidden;
    background: var(--page);
  }
  .canvas {
    position: relative;
    width: 976px;
    height: 1200px;
  }
  .sign {
    position: absolute;
    left: 38px;
    top: 374px;
    width: 900px;
    height: 451px;
    border: 1px solid #222;
  }
  .sign__brand {
    height: 273px;
    background: var(--charcoal);
    display: flex;
    align-items: center;
    justify-content: center;
    gap: 56px;
  }
  .brand-mark {
    width: 112px;
    height: 112px;
    background: var(--brand-blue);
    flex: none;
  }
  .brand-name {
    font-family: "Unbounded", sans-serif;
    font-weight: 900;
    font-size: 108px;
    line-height: 1;
    letter-spacing: -1px;
    color: var(--white);
  }
  .sign__contact {
    height: 176px;
    background: var(--brand-blue);
    display: flex;
    flex-direction: column;
    align-items: center;
    justify-content: center;
    gap: 4px;
    color: var(--white);
    font-family: "Unbounded", sans-serif;
    white-space: nowrap;
  }
  .contact__label {
    font-weight: 800;
    font-size: 48px;
    line-height: 1.1;
    letter-spacing: 1px;
  }
  .contact__phone {
    font-weight: 900;
    font-size: 80px;
    line-height: 1.1;
    letter-spacing: 2px;
  }
</style>
</head>
<body>
  <main class="canvas">
    <section class="sign">
      <div class="sign__brand">
        <div class="brand-mark"></div>
        <h1 class="brand-name">TALLON</h1>
      </div>
      <div class="sign__contact">
        <p class="contact__label">CALL FOR ASSISTANCE</p>
        <p class="contact__phone">403-555-0182</p>
      </div>
    </section>
  </main>
</body>
</html>
```